Need a slogan for Plavoria.net

Selling door knobs for kitchens, bathrooms, closets, garages, etc. Looking for a great slogan to incorporate with the logo. This is an E-commerce website and it must be very professional. Quick cash

```html
<!DOCTYPE html>
<html lang="en">
<head>
<meta charset="UTF-8">
<title>Plavoria.net — Slogan</title>
<link href="https://fonts.googleapis.com/css2?family=Carlito:wght@400&display=swap" rel="stylesheet">
<style>
  :root {
    --bg: #000000;
    --ink: #ffffff;
  }
  html, body {
    margin: 0;
    padding: 0;
    width: 1200px;
    height: 900px;
    overflow: hidden;
    background: var(--bg);
  }
  .slogan-card {
    position: relative;
    width: 1200px;
    height: 900px;
    background: var(--bg);
    color: var(--ink);
    font-family: "Carlito", "Calibri", sans-serif;
    font-weight: 400;
    text-align: center;
  }
  .tagline {
    position: absolute;
    top: 273px;
    left: 0;
    width: 1200px;
    margin: 0;
    font-size: 66px;
    font-weight: 400;
    line-height: 74px;
  }
  .brand-name {
    position: absolute;
    top: 476px;
    left: 0;
    width: 1200px;
    margin: 0;
    font-size: 132px;
    font-weight: 400;
    line-height: 150px;
  }
</style>
</head>
<body>
  <main class="slogan-card">
    <p class="tagline">Finely crafted knobs for every door in<br>your home</p>
    <h1 class="brand-name">Plavoria.net</h1>
  </main>
</body>
</html>
```